Dutch psychology podcast needs logo / art design

I need a logo / artwork for my new podcast on psychology/health called 'Het Stille Kompas'. In the podcast I talk to different experts on subjects as personal development, psychology, health, spirituality and entrepreneurship. I would like to see my brand colors back in the design (www.joristeulinghof.nl) and my face in the artwork since I'm the host of the show.

My photo is included in the attachments and I've also added some examples of what I'm looking for.

Industry/Entity Type

Psychology

Colors

Designer to choose colors to be used in the design.

Requirements
Must have
• - Name of the show: 'Het Stille Kompas' (I prefer that this name is turned into a logo), see attachment of example of Harbor of Quiet Minds
• - Subtitle: 'met Joris Teulinghof' which is my name a the host
• - My picture, see attachments

```html
<!DOCTYPE html>
<html lang="nl">
<head>
<meta charset="utf-8">
<title>Het Stille Kompas – podcast artwork</title>
<link rel="stylesheet" href="https://fonts.googleapis.com/css2?family=Montserrat:wght@800&display=swap">
<style>
  :root {
    --sun: #f9a916;
    --sun-deep: #f28a10;
    --brand-red: #d8190b;
    --circle-red: #e0210d;
    --circle-dark: #c3100a;
    --white: #ffffff;
    --accent-yellow: #f9a916;
    --portrait-top: #c99a80;
    --portrait-bottom: #1c2233;
  }
  html, body {
    margin: 0;
    padding: 0;
    overflow: hidden;
    background: var(--sun);
  }
  .cover {
    position: relative;
    width: 1200px;
    height: 1200px;
    overflow: hidden;
    background:
      radial-gradient(ellipse at 0% 20%, var(--sun-deep) 0%, rgba(242,138,16,0) 45%),
      radial-gradient(ellipse at 20% 0%, var(--sun-deep) 0%, rgba(242,138,16,0) 35%),
      var(--sun);
    font-family: "Montserrat", sans-serif;
  }
  .cover svg { position: absolute; inset: 0; }
  .show-title {
    position: absolute;
    right: 82px;
    top: 240px;
    margin: 0;
    text-align: right;
    color: var(--brand-red);
    font-weight: 800;
    font-size: 90px;
    line-height: 94px;
    letter-spacing: -1px;
    text-transform: uppercase;
  }
  .host-credit {
    position: absolute;
    right: 62px;
    top: 790px;
    margin: 0;
    text-align: right;
    color: var(--white);
    font-weight: 800;
    font-size: 62px;
    line-height: 65px;
    text-transform: uppercase;
  }
  .host-credit::after {
    content: "";
    display: block;
    margin-left: auto;
    margin-top: 12px;
    width: 285px;
    height: 4px;
    background: var(--accent-yellow);
  }
</style>
</head>
<body>
<main class="cover">
  <svg width="1200" height="1200" viewBox="0 0 1200 1200">
    <defs>
      <linearGradient id="portrait-tone" x1="0" y1="0" x2="0" y2="1">
        <stop offset="0" stop-color="var(--portrait-top)"/>
        <stop offset="0.45" stop-color="var(--portrait-top)"/>
        <stop offset="0.55" stop-color="var(--portrait-bottom)"/>
        <stop offset="1" stop-color="var(--portrait-bottom)"/>
      </linearGradient>
    </defs>

    <!-- plain corner badge -->
    <circle class="corner-badge" cx="62" cy="60" r="38" fill="none" stroke="var(--brand-red)" stroke-width="4"/>

    <!-- title frame -->
    <path class="title-frame" d="M830 218 H587 V528 H1158 V218 H920"
          fill="none" stroke="var(--brand-red)" stroke-width="5"/>

    <!-- overlapping circles -->
    <circle cx="965" cy="915" r="265" fill="var(--circle-red)"/>
    <circle cx="1125" cy="880" r="190" fill="var(--circle-dark)" opacity="0.75"/>

    <!-- host portrait area -->
    <g role="img" aria-label="Portretfoto van host Joris Teulinghof, glimlachend met armen over elkaar, donkere trui">
      <path d="M200 690 C 195 560, 205 470, 205 300 C 200 160, 300 80, 400 85 C 520 90, 550 190, 525 330 C 520 430, 500 520, 470 600 C 620 640, 720 700, 760 800 L 835 1200 L 0 1200 L 0 700 Z"
            fill="var(--brand-red)"/>
      <path d="M225 680 C 225 560, 235 470, 235 310 C 235 170, 320 95, 410 100 C 515 105, 540 200, 520 330 C 510 440, 495 520, 485 590 C 620 630, 730 690, 770 800 L 825 1200 L 0 1200 L 0 700 Z"
            fill="url(#portrait-tone)" stroke="var(--white)" stroke-width="5"/>
    </g>
  </svg>

  <h1 class="show-title">Het<br>Stille<br>Kompas</h1>
  <p class="host-credit">Met<br>Joris<br>Teulinghof</p>
</main>
</body>
</html>
```